Technology management company looking for a new website with a professional look

Brennick IT is a recently re-branded technology management company that is looking for a website design to match its personalized approach and friendly culture.

We would like to see a specialized, but related, page style for each of our main service offerings of:

• Commercial IT Support (This is our primary focus)
• Commercial Phone Systems (We partner with http://www.voxtrell.com/ for our phone systems)
• Point of Sale Systems (We partner with http://www.tillmora.com/ for our POS systems.
• Web Design
• Hollow Pine Computers (Our residential computer service offering, branded as Hollow Pine Computers)

The Hollow Pine Computers page should be build upon the Hollow Pine Computers logo, the other four pages should be branded as Brennick IT.

These five separate pages should have subtle, yet clearly defined links to one another. They should also each have a Home, Products, Service, and Company in the menu.

The website should have a clean design with professional appeal, but not appear too sterile or uninviting. It needs to have a simple, easy to navigate menu interface along the top. We would also like the site to be mobile friendly.

It should also allow us to easily tie in links to our social media pages (Facebook, LinkedIn, Twitter and Google+) and provide easy access to our contact information from each page.

This is a link to our old website www.hollowpinecomputers.com

We don't currently have copy available. The text and menu design should be easily editable and expandable so we can use the design to fit our copy.

In general we are looking for a concept we can modify to fit our needs.

We need this design to be available with layers in a .psd format.

Target Market(s)

Small to mid-size businesses.

Industry/Entity Type

Information Technology

Number of Pages Required

5+ page

Font styles to use
Sans Serif

Requirements
Must have
• Mobile Friendly
• Professional Type Face
• Unity between all pages
• .PSD Format
Nice to have
• Themed with our logo
Should not have
• Bubbly unprofessional typeface. No comic sans.

```html
<!DOCTYPE html>
<html lang="en">
<head>
<meta charset="utf-8">
<title>Brennick IT</title>
<link rel="stylesheet" href="https://fonts.googleapis.com/css2?family=Raleway:wght@400;500;600;700&family=Open+Sans:wght@400;600&display=swap">
<style>
:root{
  --accent:#e2452d;
  --ink:#333333;
  --muted:#7a7a7a;
  --dark:#161414;
  --dark-2:#221f1f;
  --line:#dcdcdc;
  --soft:#f3f3f3;
  --white:#ffffff;
  --social:#2b7fc4;
}
*{box-sizing:border-box;margin:0;padding:0}
html,body{width:800px;height:1200px;overflow:hidden}
body{background:var(--white);font-family:"Open Sans",Arial,sans-serif;color:var(--ink);position:relative}
.utility-bar{height:22px;background:var(--dark);display:flex;justify-content:center;gap:0}
.utility-bar a{font:600 9px "Raleway",sans-serif;color:#ddd;text-decoration:none;padding:0 22px;line-height:22px;letter-spacing:.5px}
.utility-bar a.is-active{background:var(--accent);color:var(--white)}
.site-header{height:78px;display:flex;align-items:center;padding:0 120px 0 120px;border-bottom:1px solid var(--line)}
.brand{display:flex;align-items:center;gap:8px;font:700 26px "Raleway",sans-serif;color:var(--ink);margin-right:auto}
.brand-dot{width:22px;height:22px;border-radius:50%;background:var(--accent)}
.service-nav{display:flex;gap:22px;align-items:center}
.service-nav a{font:500 10px/1.25 "Raleway",sans-serif;color:var(--ink);text-decoration:none;width:74px}
.search-icon{margin-left:10px}
.hero{position:relative;height:287px;background:linear-gradient(135deg,#cfd3d6 0%,#8e969c 45%,#5b6268 100%)}
.hero-text{position:absolute;left:0;right:0;top:82px;text-align:center;font:500 28px/1.25 "Raleway",sans-serif;color:var(--white);letter-spacing:.5px}
.hero-text .hl{color:var(--accent);font-weight:700}
.hero-arrow{position:absolute;top:126px}
.hero-arrow.left{left:40px}.hero-arrow.right{right:40px}
.welcome{text-align:center;padding:38px 128px 0}
.section-title{font:600 26px "Raleway",sans-serif;color:var(--ink);letter-spacing:1px}
.tagline{font-size:9.5px;color:var(--muted);margin-top:4px}
.welcome-copy{font-size:9px;line-height:1.55;color:var(--muted);margin-top:14px}
.title-rule{width:60px;height:2px;background:var(--accent);margin:12px auto 0}
.services{display:flex;justify-content:center;margin-top:22px}
.service-tile{width:136px;height:116px;border:1px solid var(--line);background:var(--soft);display:flex;flex-direction:column;align-items:center;justify-content:center;gap:10px;margin-left:-1px}
.service-tile.is-active{background:#e4e4e4;border-bottom:3px solid var(--accent)}
.service-tile .label{font:500 10px/1.25 "Raleway",sans-serif;color:var(--muted);text-align:center;text-transform:uppercase}
.service-tile.is-active .label{color:var(--ink)}
.partner-name{display:flex;align-items:center;gap:5px;font:700 15px "Raleway",sans-serif;color:var(--ink)}
.partner-name .sq{width:10px;height:10px;background:var(--accent)}
.contact{position:absolute;top:728px;left:0;right:0;height:176px;background:var(--soft);text-align:center;padding-top:16px;border-top:1px solid var(--line)}
.contact-card{width:560px;margin:14px auto 0;background:var(--white);border:1px solid var(--line);padding:12px 16px;text-align:left}
.contact-card .brand{font-size:16px;gap:6px}
.contact-card .brand-dot{width:14px;height:14px}
.contact-cols{display:flex;justify-content:space-between;margin-top:8px}
.contact-cols h4{font:700 8px "Raleway",sans-serif;color:var(--accent);text-transform:uppercase}
.contact-cols p{font-size:8px;line-height:1.5;color:var(--muted)}
.contact-cols .ico{display:flex;align-items:center;gap:4px}
.site-footer{position:absolute;top:938px;left:0;right:0;bottom:0;background:var(--dark-2);text-align:center}
.footer-nav{display:flex;justify-content:center;gap:60px;padding-top:14px;border-bottom:1px solid #3a3636;padding-bottom:10px}
.footer-nav a{font:600 9px "Raleway",sans-serif;color:#ccc;text-decoration:none}
.footer-nav a.is-active{color:var(--accent)}
.site-footer .brand{justify-content:center;color:var(--white);font-size:22px;margin:26px 0 0}
.copyright{font-size:8.5px;color:#aaa;margin-top:8px}
.footer-copy{font-size:8px;line-height:1.5;color:#8a8585;width:560px;margin:10px auto 0}
.social{display:flex;justify-content:center;gap:10px;margin-top:14px}
.social span{width:20px;height:20px;border-radius:50%;background:#5a5555}
.social span.is-active{background:var(--social)}
.legal{margin-top:16px;font-size:8px;color:#aaa}
.legal a{color:#aaa;text-decoration:underline;margin:0 8px}
</style>
</head>
<body>
<nav class="utility-bar">
  <a href="#" class="is-active">HOME</a><a href="#">PRODUCTS</a><a href="#">SERVICE</a><a href="#">COMPANY</a>
</nav>
<header class="site-header">
  <div class="brand"><span class="brand-dot"></span>Brennick IT</div>
  <nav class="service-nav">
    <a href="#">Commercial IT Support</a>
    <a href="#">Commercial Phone Systems</a>
    <a href="#">Point of Sale Systems</a>
    <a href="#">Hollow Pine Computers</a>
    <svg class="search-icon" width="16" height="16" viewBox="0 0 16 16"><circle cx="6.5" cy="6.5" r="5" fill="none" stroke="#333" stroke-width="1.6"/><line x1="10.2" y1="10.2" x2="15" y2="15" stroke="#333" stroke-width="1.8"/></svg>
  </nav>
</header>
<section class="hero" role="img" aria-label="Photo of a team working at a desk with laptops, tablets and charts">
  <svg class="hero-arrow left" width="12" height="22" viewBox="0 0 12 22"><polyline points="10,2 2,11 10,20" fill="none" stroke="#fff" stroke-width="2"/></svg>
  <p class="hero-text">COST-EFFECTIVE SOLUTIONS -<br><span class="hl">RELATIONSHIP</span><br>COMMUNICATION</p>
  <svg class="hero-arrow right" width="12" height="22" viewBox="0 0 12 22"><polyline points="2,2 10,11 2,20" fill="none" stroke="#fff" stroke-width="2"/></svg>
</section>
<section class="welcome">
  <h2 class="section-title">WELCOME</h2>
  <p class="tagline">Our goal is to build a relationship with our clients, communicate clearly, and find timely, cost-effective solutions to your needs.</p>
  <p class="welcome-copy">We support local businesses with dependable technology, from network care and help desk service to phone systems and point of sale setups. Our team plans upgrades, watches your systems around the clock, and answers quickly when something goes wrong. We keep pricing clear and simple, explain every option in plain words, and treat each client like a neighbor. Whether you run one office or several, we shape our service to fit your goals and your budget.</p>
  <div class="title-rule"></div>
</section>
<section class="services">
  <div class="service-tile">
    <svg width="38" height="34" viewBox="0 0 38 34"><g fill="none" stroke="#888" stroke-width="3"><circle cx="13" cy="19" r="7"/><circle cx="28" cy="9" r="5"/></g><g stroke="#888" stroke-width="3"><line x1="13" y1="7" x2="13" y2="10"/><line x1="13" y1="28" x2="13" y2="31"/><line x1="1" y1="19" x2="4" y2="19"/><line x1="22" y1="19" x2="25" y2="19"/></g></svg>
    <span class="label">Commercial<br>IT Support</span>
  </div>
  <div class="service-tile is-active">
    <span class="partner-name"><span class="sq"></span>Voxtrell</span>
    <span class="label">Commercial<br>Phone Systems</span>
  </div>
  <div class="service-tile">
    <svg width="36" height="32" viewBox="0 0 36 32"><rect x="4" y="2" width="28" height="18" rx="2" fill="none" stroke="#888" stroke-width="2.5"/><rect x="14" y="20" width="8" height="5" fill="#888"/><rect x="6" y="25" width="24" height="5" rx="1" fill="#888"/></svg>
    <span class="label">Point of<br>Sale Systems</span>
  </div>
  <div class="service-tile">
    <span class="partner-name" style="font-size:11px;color:#888"><span class="sq" style="background:#888"></span>Hollow Pine</span>
    <span class="label">Hollow Pine<br>Computers</span>
  </div>
</section>
<section class="contact">
  <h2 class="section-title">CONTACT US</h2>
  <p class="tagline">Our goal is to build a relationship with our clients, communicate clearly, and find timely, cost-effective solutions to your needs.</p>
  <div class="contact-card">
    <div class="brand"><span class="brand-dot"></span>Brennick IT</div>
    <div class="contact-cols">
      <div><h4>Office Address</h4><p>1510 S. Fern St.<br>Suite A, Middleton, PA 15540</p></div>
      <div>
        <p class="ico"><svg width="8" height="8" viewBox="0 0 8 8"><rect x="2" y="0" width="4" height="8" rx="1" fill="#e2452d"/></svg>000-555-0101</p>
        <p class="ico"><svg width="8" height="8" viewBox="0 0 8 8"><rect x="2" y="0" width="4" height="8" rx="1" fill="#e2452d"/></svg>000-555-0102</p>
        <p class="ico"><svg width="8" height="8" viewBox="0 0 8 8"><rect x="0" y="1" width="8" height="6" fill="#e2452d"/></svg>info@brennickit.com</p>
      </div>
      <div><h4>Office Hours</h4><p>Monday-Friday, 8am to 6pm<br>Saturday, 9am to 1pm</p></div>
    </div>
  </div>
</section>
<footer class="site-footer">
  <nav class="footer-nav"><a href="#" class="is-active">HOME</a><a href="#">PRODUCTS</a><a href="#">SERVICE</a><a href="#">COMPANY</a></nav>
  <div class="brand"><span class="brand-dot"></span>Brennick IT</div>
  <p class="copyright">Copyright © 2015 Brennick IT Inc. All rights reserved.</p>
  <p class="footer-copy">Brennick IT provides managed support, phone systems, point of sale and web design for small and mid-size businesses. Reach out any time to learn how our team can keep your office connected, secure and running smoothly every day.</p>
  <div class="social"><span></span><span></span><span class="is-active"></span><span></span></div>
  <p class="legal"><a href="#">Terms of use</a>|<a href="#">Privacy Policy</a>|<a href="#">Get Registered</a></p>
</footer>
</body>
</html>
```